Flyer Design Project

We need a flyer (in Spanish) for:
"Feria Cántaro & Telar Brisa Alta 2013"
This event will be held in Los Angeles CA and would like to attract exhibitors.
Must include the information provided in the word file.
Updates

Target Market(s)

Tequila producers and distributors

Industry/Entity Type

Event

Requirements
Must have
• pictures to be used at your discretion

```html
<!DOCTYPE html>
<html lang="es">
<head>
<meta charset="utf-8">
<title>Feria Cántaro &amp; Telar Brisa Alta 2013</title>
<link rel="stylesheet" href="https://fonts.googleapis.com/css2?family=Cinzel:wght@700&family=Jost:wght@500;600;700&family=Pinyon+Script&display=swap">
<style>
  :root {
    --page: #ffffff;
    --parchment-light: #f3e7c4;
    --parchment-mid: #e6d29e;
    --parchment-dark: #c9ad6e;
    --title-brown: #5b3a17;
    --ink: #1d1408;
    --script-ink: #2a1a0a;
    --wood-dark: #4a3520;
    --wood-light: #8a6c48;
    --photo-agave: #6f7a5a;
    --photo-cellar: #7c6048;
    --photo-pottery: #b8642a;
    --photo-crowd: #8a6a58;
    --glass: #d9c78a;
  }
  * { box-sizing: border-box; margin: 0; padding: 0; }
  html, body { width: 1200px; height: 1000px; overflow: hidden; background: var(--page); }
  .canvas { position: relative; width: 1200px; height: 1000px; }

  .flyer {
    position: absolute; left: 228px; top: 25px; width: 734px; height: 950px;
    background:
      radial-gradient(ellipse at 50% 40%, var(--parchment-light) 0%, var(--parchment-mid) 60%, var(--parchment-dark) 100%);
    overflow: hidden;
  }

  .photo-strip { position: absolute; left: 0; top: 0; width: 734px; height: 176px; }
  .frame-band {
    position: absolute; left: 0; width: 734px;
    background: linear-gradient(180deg, var(--wood-light), var(--wood-dark) 50%, var(--wood-light));
  }
  .frame-band.top { top: 0; height: 20px; }
  .frame-band.bottom { top: 163px; height: 13px; }
  .photo { position: absolute; top: 20px; height: 143px; }
  .photo.agave { left: 0; width: 165px; background: linear-gradient(180deg, #a9b7a8 0%, var(--photo-agave) 45%, #3f4a35 100%); }
  .photo.cellar { left: 165px; width: 195px; background: linear-gradient(90deg, #3a2a1c 0%, var(--photo-cellar) 45%, #e4ded2 70%, #5a4430 100%); }
  .photo.pottery { left: 360px; width: 182px; background: radial-gradient(ellipse at 50% 55%, #d98a3f 0%, var(--photo-pottery) 55%, #6a3516 100%); }
  .photo.crowd { left: 542px; width: 192px; background: linear-gradient(90deg, #c9a890 0%, var(--photo-crowd) 50%, #5a3e30 100%); }

  .event-title {
    position: absolute; left: 0; top: 188px; width: 734px; text-align: center;
    font-family: "Cinzel", Georgia, serif; font-weight: 700; color: var(--title-brown);
    text-shadow: 1px 1px 2px rgba(80, 50, 20, 0.35);
  }
  .event-title .line-one { display: block; font-size: 44px; line-height: 52px; }
  .event-title .line-two { display: block; font-size: 34px; line-height: 44px; }

  .tagline {
    position: absolute; left: 48px; top: 294px; width: 640px;
    font-family: "Pinyon Script", cursive; font-size: 29px; line-height: 32px;
    color: var(--script-ink);
  }
  .tagline .second { display: block; padding-left: 14px; }

  .body-copy {
    position: absolute; left: 49px; top: 380px; width: 632px;
    font-family: "Jost", Arial, sans-serif; font-weight: 500; font-size: 14.2px; line-height: 21px;
    color: var(--ink);
  }
  .body-copy p { margin-bottom: 12px; }

  .contact-lead {
    position: absolute; left: 52px; top: 786px;
    font-family: "Jost", Arial, sans-serif; font-weight: 600; font-size: 14.2px; color: var(--ink);
  }
  .contact {
    position: absolute; top: 820px;
    font-family: "Jost", Arial, sans-serif; font-weight: 500; font-size: 12.4px; line-height: 19px; color: var(--ink);
  }
  .contact.usa { left: 169px; }
  .contact.mexico { left: 435px; }
  .glass-icon { position: absolute; left: 340px; top: 812px; width: 48px; height: 70px; }

  .website {
    position: absolute; left: 0; top: 893px; width: 734px; text-align: center;
    font-family: "Jost", Arial, sans-serif; font-weight: 700; font-size: 22px; color: var(--ink);
  }
</style>
</head>
<body>
<div class="canvas">
  <article class="flyer">
    <div class="photo-strip">
      <div class="frame-band top"></div>
      <div class="photo agave" role="img" aria-label="Fotografía de un campo de agave con un jimador"></div>
      <div class="photo cellar" role="img" aria-label="Fotografía de productores catando en una bodega de barricas"></div>
      <div class="photo pottery" role="img" aria-label="Fotografía de vasijas de barro artesanales"></div>
      <div class="photo crowd" role="img" aria-label="Fotografía de un grupo de amigos brindando"></div>
      <div class="frame-band bottom"></div>
    </div>

    <h1 class="event-title">
      <span class="line-one">Feria Cántaro &amp; Telar</span>
      <span class="line-two">Brisa Alta 2013</span>
    </h1>

    <p class="tagline">¡Vinculando marcas emergentes e innovadoras en una <span class="second">época de descubrimiento de sabores mundiales!</span></p>

    <div class="body-copy">
      <p>Chile, España, Escocia, Francia, Argentina, Polonia, Mexico – cuando buscamos que beber, buscamos en el mundo, y ese mundo termina en nuestros vasos. Queremos lo mejor, lo más sabroso, lo interesante y estamos dispuestos a recorrer grandes distancias para obtenerlo.</p>
      <p>&nbsp;La promoción y la creatividad son, quizás, aún más importante en tiempos de incertidumbre económica,<br>cuando se es implacable en la búsqueda de nuevos clientes. Con unas perspectivas más amplias, más globales, ya sea sondeando tradiciones centenarias, o la exploración de las fronteras de las bebidas de moda, buscando nuevas mercados, o re-inventando su marca para mantenerse competitivos.</p>
      <p>En esta edición especializada en Tequila, vamos a discutir las técnicas, procesos creativos, perfiles de sabor, tecnologías, y los ingredientes que son cada vez más esenciales de la caja de herramientas del Coctelero (Mixologist) del siglo 21.</p>
      <p>Tendremos una competencia de las cuatro variedades de tequila: Blanco, Reposado, Añejo y Extra Añejo; con reconocimiento a los ganadores de cada categoría.</p>
      <p>Acompáñanos, los días 29 y 30 de agosto 2013, donde se vincularan, consumidores, bares, detallistas, restaurantes y distribuidores, en la matriz de creatividad coctelera, talento culinario, sabores de moda &nbsp;y uno de los mercados más importantes e influyentes &nbsp;del mundo.</p>
    </div>

    <p class="contact-lead">Para oportunidades de patrocinio y exhibición:</p>

    <address class="contact usa" style="font-style:normal">
      (USA)<br>Rogelio T. Ibarra – Director<br>Tel. + 818-555-0142<br>ribarra@ferianube.com
    </address>

    <svg class="glass-icon" viewBox="0 0 48 70" aria-hidden="true">
      <path d="M4 4 L44 4 L40 66 L8 66 Z" fill="#f4ecd0" fill-opacity="0.6" stroke="#b9a874" stroke-width="2"/>
      <path d="M7 24 L41 24 L39 64 L9 64 Z" fill="var(--glass)"/>
    </svg>

    <address class="contact mexico" style="font-style:normal">
      (Mexico)<br>Ing. Ernesto L. Vidal<br>Tel. 333-555-0187<br>evidal@ferianube.com
    </address>

    <p class="website">www.ferianube.com</p>
  </article>
</div>
</body>
</html>
```